Creative Brief
Stationery and Cards
Need clean, simple, modern cards/letterhead
Simple
Dale Pruett
Executive Direstor
418 Hollister Avenue
Suite 214
Larkfield, NY 11742
Dpruett@brimlow.com
www.mistvaleloft.com

```html
<!DOCTYPE html>
<html lang="en">
<head>
<meta charset="utf-8">
<title>Mistvale business cards</title>
<link href="https://fonts.googleapis.com/css2?family=Open+Sans:wght@400;600;700&display=swap" rel="stylesheet">
<style>
  :root{
    --bg:#ecebe8;
    --card:#ffffff;
    --ink:#3d3d3d;
    --blue:#2bb5e3;
    --orange:#f6a623;
    --green:#8cc63f;
    --rule:#d5d5d5;
  }
  *{box-sizing:border-box;margin:0;padding:0}
  html,body{width:1200px;height:852px;overflow:hidden;background:var(--bg);font-family:"Open Sans",Arial,sans-serif;color:var(--ink)}
  .stage{position:relative;width:1200px;height:852px;display:flex;align-items:center;justify-content:center;gap:40px}
  .card{position:relative;width:540px;height:309px;background:var(--card);border-radius:16px;overflow:hidden;box-shadow:0 6px 18px rgba(0,0,0,.15)}
  .card__bands{position:absolute;left:0;right:0;bottom:0;height:20px}
  .card__bands::before{content:"";position:absolute;left:0;right:0;top:0;height:4px;background:var(--orange)}
  .card__bands::after{content:"";position:absolute;left:0;right:0;bottom:0;height:14px;background:var(--blue)}
  .brand{display:flex;flex-direction:column;align-items:center;gap:8px}
  .brand__dot{width:46px;height:46px;border-radius:50%;background:var(--blue)}
  .brand__name{font-weight:600;font-size:34px;letter-spacing:3px;text-transform:uppercase;color:var(--ink);line-height:1}
  .person__name{font-weight:700;font-size:15px}
  .person__title{font-weight:600;font-size:12px;color:var(--orange);margin-bottom:6px}
  .person__addr{font-size:12.5px;line-height:1.45}
  .contacts{list-style:none;font-size:12.5px}
  .contacts li{display:flex;align-items:center;gap:8px;line-height:1.9}
  .contacts svg{width:14px;height:14px;flex:none}
  .divider{width:1px;background:var(--rule);align-self:stretch}

  .card--centered .brand{position:absolute;top:30px;left:0;right:0}
  .card--centered .details{position:absolute;top:160px;left:0;right:0;display:flex;justify-content:center;gap:18px}
  .card--centered .person{text-align:right}
  .card--centered .person__name{color:var(--orange)}

  .card--split .details{position:absolute;top:50px;left:282px;display:flex;gap:16px}
  .card--split .person__name{color:var(--green)}
  .card--split .stack{display:flex;flex-direction:column;gap:14px}
  .card--split .brand{position:absolute;left:32px;top:150px}
  .card--split .brand__name{font-size:28px}
</style>
</head>
<body>
<main class="stage">

  <article class="card card--centered">
    <div class="brand">
      <span class="brand__dot"></span>
      <span class="brand__name">Mistvale</span>
    </div>
    <div class="details">
      <div class="person">
        <p class="person__name">Dale Pruett</p>
        <p class="person__title">Executive Director</p>
        <p class="person__addr">418 Hollister Avenue, Suite 214<br>Larkfield, NY 11742</p>
      </div>
      <span class="divider"></span>
      <ul class="contacts">
        <li><svg viewBox="0 0 14 14"><circle cx="7" cy="7" r="7" fill="var(--blue)"/><rect x="4.5" y="3" width="5" height="8" rx="1" fill="#fff"/></svg>917-555-0148</li>
        <li><svg viewBox="0 0 14 14"><circle cx="7" cy="7" r="7" fill="var(--blue)"/><text x="7" y="10" font-size="9" text-anchor="middle" fill="#fff" font-family="Arial">@</text></svg>Dpruett@brimlow.com</li>
        <li><svg viewBox="0 0 14 14"><circle cx="7" cy="7" r="7" fill="var(--blue)"/><circle cx="7" cy="7" r="3.8" fill="none" stroke="#fff" stroke-width="1"/><path d="M3.2 7h7.6M7 3.2v7.6" stroke="#fff" stroke-width="1"/></svg>www.mistvaleloft.com</li>
      </ul>
    </div>
    <div class="card__bands"></div>
  </article>

  <article class="card card--split">
    <div class="details">
      <span class="divider"></span>
      <div class="stack">
        <div class="person">
          <p class="person__name">Dale Pruett</p>
          <p class="person__title">Executive Director</p>
          <p class="person__addr">418 Hollister Avenue, Suite 214<br>Larkfield, NY 11742</p>
        </div>
        <ul class="contacts">
          <li><svg viewBox="0 0 14 14"><circle cx="7" cy="7" r="7" fill="var(--blue)"/><rect x="4.5" y="3" width="5" height="8" rx="1" fill="#fff"/></svg>917-555-0148</li>
          <li><svg viewBox="0 0 14 14"><circle cx="7" cy="7" r="7" fill="var(--blue)"/><text x="7" y="10" font-size="9" text-anchor="middle" fill="#fff" font-family="Arial">@</text></svg>Dpruett@brimlow.com</li>
          <li><svg viewBox="0 0 14 14"><circle cx="7" cy="7" r="7" fill="var(--blue)"/><circle cx="7" cy="7" r="3.8" fill="none" stroke="#fff" stroke-width="1"/><path d="M3.2 7h7.6M7 3.2v7.6" stroke="#fff" stroke-width="1"/></svg>www.mistvaleloft.com</li>
        </ul>
      </div>
    </div>
    <div class="brand">
      <span class="brand__dot"></span>
      <span class="brand__name">Mistvale</span>
    </div>
    <div class="card__bands"></div>
  </article>

</main>
</body>
</html>
```